Card for Real Estate Developer

We need a business card design for a Real Estate Development company based in Texas. We focus on retail, apartment and residential development. Our target is predominantly investors looking to us to place their money properly to achieve a significant return. On the other side we sell our services to large retailers as their preferred developer assisting them in locating, building and leasing their real estate.

Target Market(s)

Investors

Industry/Entity Type

Real Estate Development

Contact Information for Business Card

Would like to stay within the company color scheme, while keeping the design moderately simple.

Font styles to use
Other font styles liked:
• per attached document

Requirements
Must have
• Name
• Phone
• Email
• Website
• Logo Prominently Displayed
• Stay within the colors provided in the attached document

```html
<!DOCTYPE html>
<html lang="en">
<head>
<meta charset="utf-8">
<title>Brazos Ridge Development – Business Card</title>
<link href="https://fonts.googleapis.com/css2?family=Open+Sans:wght@400;600;700&display=swap" rel="stylesheet">
<style>
  :root {
    --page-bg: #f7f7f7;
    --card-white: #ffffff;
    --brand-blue: #3f8fbf;
    --brand-blue-light: #6cb0d0;
    --brand-blue-deep: #4a8ab8;
    --ink-dark: #3a3a3a;
    --ink-muted: #555555;
    --rule-blue: #5a9fc6;
  }
  * { box-sizing: border-box; margin: 0; padding: 0; }
  html, body {
    width: 1200px; height: 1000px; overflow: hidden;
    background: var(--page-bg);
    font-family: "Open Sans", Arial, sans-serif;
  }
  .canvas {
    position: relative; width: 1200px; height: 1000px;
  }
  .card {
    position: absolute;
    width: 640px; height: 366px;
    border-radius: 34px;
    box-shadow: 0 10px 30px rgba(0,0,0,0.12);
    overflow: hidden;
  }
  /* Back side: contact details */
  .card-back {
    left: 460px; top: 90px;
    background: var(--card-white);
  }
  .back-brand {
    position: absolute; right: 56px; top: 62px;
    display: flex; align-items: center; gap: 12px;
    color: var(--brand-blue);
    font-weight: 600; font-size: 22px; letter-spacing: 0.5px;
  }
  .brand-mark-square {
    width: 26px; height: 26px; background: currentColor;
  }
  .back-rule {
    position: absolute; left: 110px; right: 56px; top: 150px;
    height: 1.5px; background: var(--rule-blue);
  }
  .name-bar {
    position: absolute; left: 0; top: 184px;
    width: 8px; height: 40px; background: var(--brand-blue);
    border-radius: 0 3px 3px 0;
  }
  .person {
    position: absolute; left: 40px; top: 180px;
  }
  .person-name {
    color: var(--brand-blue); font-weight: 700; font-size: 22px; line-height: 1.1;
  }
  .person-title {
    color: var(--ink-dark); font-size: 12px; margin-top: 3px;
  }
  .contact-list {
    position: absolute; left: 40px; top: 246px;
    list-style: none;
    border-top: 1px solid #d6e3ec; padding-top: 10px; width: 300px;
  }
  .contact-item {
    display: flex; align-items: center; gap: 12px;
    color: var(--ink-muted); font-size: 13px; height: 26px;
  }
  .contact-icon { width: 15px; height: 15px; fill: var(--brand-blue); flex: none; }

  /* Front side: brand */
  .card-front {
    left: 100px; top: 520px;
    background: linear-gradient(180deg, var(--brand-blue-light) 0%, var(--brand-blue-deep) 100%);
    color: var(--card-white);
    display: flex; flex-direction: column; align-items: center; justify-content: center;
  }
  .front-brand {
    display: flex; align-items: center; gap: 16px;
    font-weight: 600; font-size: 34px; letter-spacing: 1px;
  }
  .front-brand .brand-mark-square { width: 40px; height: 40px; }
  .front-rule {
    width: 300px; height: 1.5px; background: rgba(255,255,255,0.85); margin: 18px 0 20px;
  }
  .front-website {
    font-weight: 700; font-size: 14px; letter-spacing: 0.5px;
  }
</style>
</head>
<body>
<main class="canvas">

  <section class="card card-back" aria-label="Business card back">
    <div class="back-brand">
      <span class="brand-mark-square" aria-hidden="true"></span>
      <span class="brand-name">Brazos Ridge Development</span>
    </div>
    <div class="back-rule"></div>
    <div class="name-bar"></div>
    <div class="person">
      <p class="person-name">Daniel Carver</p>
      <p class="person-title">Real Estate Developer</p>
    </div>
    <ul class="contact-list">
      <li class="contact-item">
        <svg class="contact-icon" viewBox="0 0 24 24" aria-hidden="true"><path d="M6.6 10.8a15.1 15.1 0 0 0 6.6 6.6l2.2-2.2a1 1 0 0 1 1-.25 11.4 11.4 0 0 0 3.6.57 1 1 0 0 1 1 1V20a1 1 0 0 1-1 1A17 17 0 0 1 3 4a1 1 0 0 1 1-1h3.5a1 1 0 0 1 1 1c0 1.25.2 2.45.57 3.57a1 1 0 0 1-.25 1z"/></svg>
        <span>979-555-0148</span>
      </li>
      <li class="contact-item">
        <svg class="contact-icon" viewBox="0 0 24 24" aria-hidden="true"><path d="M2 5h20v14H2z M2 5l10 8 10-8" fill="none" stroke="#3f8fbf" stroke-width="2"/><path d="M3 6l9 7 9-7v12H3z"/></svg>
        <span>dcarver@brazosridge.com</span>
      </li>
      <li class="contact-item">
        <svg class="contact-icon" viewBox="0 0 24 24" aria-hidden="true"><circle cx="12" cy="12" r="10"/><path d="M2 12h20M12 2c3 3 3 17 0 20M12 2c-3 3-3 17 0 20" fill="none" stroke="#fff" stroke-width="1.4"/></svg>
        <span>brazosridge.com</span>
      </li>
    </ul>
  </section>

  <section class="card card-front" aria-label="Business card front">
    <div class="front-brand">
      <span class="brand-mark-square" aria-hidden="true"></span>
      <span class="brand-name">Brazos Ridge Development</span>
    </div>
    <div class="front-rule"></div>
    <p class="front-website">WWW.BRAZOSRIDGE.COM</p>
  </section>

</main>
</body>
</html>
```